Business Card for Marco Thieblin Analytics and Marco Thieblin Photography

I want a double sided business card: on one side it should be about "Marco Thieblin Photography" and on the other side about "Marco Thieblin Analytics". You find the logos for these two projects in the attachments. The design of the business card should blend well with the colours and fonts used in the logos and should be quite simple, yet look professional and modern.

In addition to my name, there should be content for a telephone number, e-mail address and website. There should be little icons (for telephone, email and web) before these fields. I do not want a postal mail address field.
Lastly you should indicate that people can contact me in the following languages: Lëtzebuergesch, Deutsch, Français, English, Castellano, Ido
This should be very unobtrusive: either in a small muted font or with little icons (preferably without using flags as flags represent nations, not languages - one possibility would be by using the 2 letter ISO codes).

The design should be delivered in Adobe Illustrator format or something similar that I can edit easily, as it's possible that I will change my e-mail address and domain soon.

I hope this was detailed enough but still leaves you some freedom for designing something nice.

Thank you!
Marco

Industry/Entity Type

Business

Contact Information for Business Card

e-mail address: mtb_@orvenmail.example
website: www.marcothieblin.example (for Marco Thieblin Photography)
website: kelvodata.example/mtb (for Marco Thieblin Analytics - this address is likely to change)
phone: +352 691 987 654 (not my real number - I prefer not to publish it on the web)

Requirements
Nice to have
• A speech bubble followed by the 2-letter language codes (lb, de, fr, en, es, io) or even speech bubble icons for every language would be nice and eliminates the need to put text like 'you can contact me in the following languages'.

```html
<!DOCTYPE html>
<html lang="en">
<head>
<meta charset="utf-8">
<title>Marco Thieblin – Business Cards</title>
<link rel="stylesheet" href="https://fonts.googleapis.com/css2?family=Open+Sans:wght@400;600;700&family=Courgette&display=swap">
<style>
  :root {
    --page: #e9e6e1;
    --card-photo: #2b2a2a;
    --card-analytics: #141414;
    --card-analytics-2: #202020;
    --orange: #f08a1c;
    --blue: #1e9ad6;
    --white: #f4f4f4;
    --muted: #8a8a8a;
    --shadow: rgba(0, 0, 0, 0.28);
  }
  * { box-sizing: border-box; margin: 0; padding: 0; }
  html, body {
    width: 1200px;
    height: 900px;
    overflow: hidden;
    background: var(--page);
    font-family: "Open Sans", Arial, sans-serif;
  }
  .stage { position: relative; width: 1200px; height: 900px; }

  .card {
    position: absolute;
    width: 600px;
    height: 343px;
    border-radius: 4px;
    box-shadow: 0 10px 28px var(--shadow);
    overflow: hidden;
  }

  /* Photography side */
  .card--photography {
    left: 70px;
    top: 100px;
    background: var(--card-photo);
    text-align: center;
  }
  .brand {
    display: flex;
    align-items: center;
    justify-content: center;
    gap: 12px;
    color: var(--orange);
    font-weight: 600;
    font-size: 30px;
    letter-spacing: 0.5px;
  }
  .brand__mark {
    width: 14px;
    height: 14px;
    border-radius: 50%;
    background: var(--blue);
  }
  .card--photography .brand { margin-top: 112px; }
  .languages__intro {
    margin-top: 40px;
    font-family: "Courgette", "Brush Script MT", cursive;
    color: var(--white);
    font-size: 19px;
  }
  .languages__list {
    margin-top: 18px;
    color: var(--orange);
    font-size: 13.5px;
    letter-spacing: 0.2px;
  }
  .languages__list .sep { color: var(--muted); margin: 0 6px; }

  /* Analytics side */
  .card--analytics {
    left: 530px;
    top: 480px;
    background: linear-gradient(100deg, var(--card-analytics) 0%, var(--card-analytics-2) 55%, var(--card-analytics) 100%);
  }
  .card--analytics .brand {
    position: absolute;
    right: 36px;
    top: 80px;
    font-size: 26px;
    justify-content: flex-end;
  }
  .card--analytics .brand__mark {
    border-radius: 0;
    background: #2fa84f;
  }
  .owner {
    position: absolute;
    left: 40px;
    top: 170px;
  }
  .owner__name {
    color: var(--orange);
    font-weight: 700;
    font-size: 25px;
    letter-spacing: 0.3px;
    margin-bottom: 10px;
  }
  .contact { list-style: none; }
  .contact__item {
    display: flex;
    align-items: center;
    gap: 14px;
    color: var(--white);
    font-size: 18px;
    line-height: 30px;
  }
  .contact__icon { width: 15px; height: 15px; flex: none; }
  .contact__icon * { fill: var(--orange); }
</style>
</head>
<body>
<main class="stage">

  <section class="card card--photography" aria-label="Photography side">
    <div class="brand"><span class="brand__mark"></span>Marco Thieblin Photography</div>
    <p class="languages__intro">Reach us in the following languages:</p>
    <p class="languages__list">
      Lëtzebuergesch<span class="sep">|</span>Deutsch<span class="sep">|</span>Français<span class="sep">|</span>English<span class="sep">|</span>Castellano<span class="sep">|</span>Ido
    </p>
  </section>

  <section class="card card--analytics" aria-label="Analytics side">
    <div class="brand"><span class="brand__mark"></span>Marco Thieblin Analytics</div>
    <div class="owner">
      <h1 class="owner__name">MARCO THIEBLIN</h1>
      <ul class="contact">
        <li class="contact__item">
          <svg class="contact__icon" viewBox="0 0 16 16" aria-hidden="true"><path d="M3.5 1 6 3.6 4.6 5.6c.9 2 2.5 3.6 4.4 4.6l2-1.4L14 11.5 12.6 14C7 14 2 9 2 3.4Z"/></svg>
          <span>+352 691 987 654</span>
        </li>
        <li class="contact__item">
          <svg class="contact__icon" viewBox="0 0 16 16" aria-hidden="true"><path d="M1 3h14v1.2L8 9 1 4.2Z"/><path d="M1 5.8 8 10.6l7-4.8V13H1Z"/></svg>
          <span>mtb_@orvenmail.example</span>
        </li>
        <li class="contact__item">
          <svg class="contact__icon" viewBox="0 0 16 16" aria-hidden="true"><path d="M8 1a7 7 0 1 0 0 14A7 7 0 0 0 8 1Zm-1 2.5c1 .3 1.5 1 1 1.8-.6.8-2 .5-2 1.7 0 1 1.8 1 2.3 2 .4 1-.5 2.2-.3 3.5C5 12 3 10 3 8c0-2 1.6-4 4-4.5Zm3.5 1.3c1.4.8 2.4 2.2 2.5 3.9-.8-.4-1.5-1.2-2.4-1-.8.2-1-.9-.6-1.6.3-.5.5-.9.5-1.3Z"/></svg>
          <span>www.marcothieblin.example</span>
        </li>
      </ul>
    </div>
  </section>

</main>
</body>
</html>
```